business cards foreign exchange student company
Bluebird Hosting
Bright & Fun-filled
Mack Dorran
Service Director
Western Region
mack@mybluebirdhosting.com
mybluebirdhosting.com
This business card needs to be unforgettable! It needs to stand out from all the other business cards. Something clever/funny. It needs to communicate this is fun!! this is exciting!! and our theme for our company is "The Best Time Ever!" so the business card should convey that they have just found The Best Time Ever!!!
This will be my new website (with the old logo)
this is a marketing piece used to send families to the website
another marketing piece to get families to the website
This is my logo .ai file
This is my .ai logo file for dark backgrounds

```html
<!DOCTYPE html>
<html lang="en">
<head>
<meta charset="utf-8">
<title>Bluebird Hosting — Business Card</title>
<link href="https://fonts.googleapis.com/css2?family=Cinzel:wght@400;700&display=swap" rel="stylesheet">
<style>
  :root {
    --backdrop: #e9e6e1;
    --card: #ffffff;
    --brand-blue: #1f5f8f;
    --band-blue-top: #2f6e9c;
    --band-blue-bottom: #164a73;
    --accent-green: #6cbf2a;
    --ink: #3a3a3a;
    --muted: #6f6f6f;
    --icon: #2a5d86;
  }
  * { box-sizing: border-box; margin: 0; padding: 0; }
  html, body {
    width: 1200px; height: 902px; overflow: hidden;
    background: var(--backdrop);
    font-family: "Cinzel", serif;
  }
  .card {
    position: absolute; left: 100px; top: 161px;
    width: 1000px; height: 580px;
    background: var(--card);
    box-shadow: 0 10px 30px rgba(0,0,0,0.18);
  }
  .brand {
    position: absolute; left: 140px; top: 78px;
    display: flex; align-items: center; gap: 18px;
  }
  .brand-dot {
    width: 86px; height: 86px; border-radius: 50%;
    background: var(--brand-blue);
  }
  .brand-name {
    font-size: 50px; font-weight: 700; color: var(--brand-blue);
    line-height: 1;
  }
  .brand-tagline {
    position: absolute; left: 350px; top: 150px;
    font-size: 20px; font-weight: 700; color: var(--ink);
    letter-spacing: 0.5px;
  }
  .person {
    position: absolute; left: 0; right: 0; top: 262px;
    text-align: center;
  }
  .person-name {
    font-size: 27px; font-weight: 700; color: var(--brand-blue);
    letter-spacing: 1px;
  }
  .person-title {
    margin-top: 4px;
    font-size: 17px; color: var(--muted); letter-spacing: 1.5px;
  }
  .contacts {
    position: absolute; left: 48px; right: 48px; top: 378px;
    font-size: 18px; color: var(--ink);
  }
  .contact-row { display: flex; gap: 22px; margin-bottom: 12px; white-space: nowrap; }
  .contact-item { display: flex; align-items: center; gap: 7px; }
  .contact-item svg { width: 18px; height: 18px; flex: none; }
  .accent-line {
    position: absolute; top: 478px; height: 14px;
    background: var(--accent-green);
  }
  .accent-line.left { left: 0; width: 240px; }
  .accent-line.right { left: 810px; right: 0; }
  .web-band {
    position: absolute; left: 240px; top: 470px;
    width: 570px; height: 84px;
    background: linear-gradient(var(--band-blue-top), var(--band-blue-bottom));
    display: flex; align-items: center; justify-content: center;
    color: #ffffff; font-size: 19px; letter-spacing: 4px;
  }
</style>
</head>
<body>
  <main class="card">
    <div class="brand">
      <div class="brand-dot"></div>
      <div class="brand-name">Bluebird Hosting</div>
    </div>
    <div class="brand-tagline">Bright &amp; Fun-filled</div>

    <section class="person">
      <div class="person-name">Mack Dorran</div>
      <div class="person-title">Service Director</div>
    </section>

    <section class="contacts">
      <div class="contact-row">
        <span class="contact-item">
          <svg viewBox="0 0 20 20"><circle cx="10" cy="10" r="10" fill="var(--icon)"/><path d="M10 4a4 4 0 0 0-4 4c0 3 4 8 4 8s4-5 4-8a4 4 0 0 0-4-4zm0 5.5a1.5 1.5 0 1 1 0-3 1.5 1.5 0 0 1 0 3z" fill="#fff"/></svg>
          Western Region
        </span>
        <span class="contact-item">
          <svg viewBox="0 0 20 20"><circle cx="10" cy="10" r="10" fill="var(--icon)"/><path d="M7 5l2 3-1 1.2c.7 1.4 1.6 2.3 2.8 2.8L12 11l3 2-1 2c-4 0-8-4-8-9z" fill="#fff"/></svg>
          8775550147
        </span>
        <span class="contact-item">
          <svg viewBox="0 0 20 20"><circle cx="10" cy="10" r="10" fill="var(--icon)"/><rect x="7" y="4" width="6" height="12" rx="1" fill="#fff"/></svg>
          8015550192
        </span>
        <span class="contact-item">
          <svg viewBox="0 0 20 20"><circle cx="10" cy="10" r="10" fill="var(--icon)"/><path d="M7 5l2 3-1 1.2c.7 1.4 1.6 2.3 2.8 2.8L12 11l3 2-1 2c-4 0-8-4-8-9z" fill="#fff"/></svg>
          18015550163
        </span>
      </div>
      <div class="contact-row">
        <span class="contact-item">
          <svg viewBox="0 0 20 20"><circle cx="10" cy="10" r="10" fill="var(--icon)"/><rect x="5" y="6" width="10" height="8" fill="#fff"/><path d="M5 6l5 4 5-4" stroke="var(--icon)" fill="none"/></svg>
          mack@mybluebirdhosting.com
        </span>
        <span class="contact-item">
          <svg viewBox="0 0 20 20"><circle cx="10" cy="10" r="10" fill="var(--icon)"/><circle cx="10" cy="10" r="5" fill="none" stroke="#fff" stroke-width="1.4"/><path d="M5 10h10M10 5v10" stroke="#fff" stroke-width="1.2"/></svg>
          www.mybluebirdhosting.com
        </span>
      </div>
    </section>

    <div class="accent-line left"></div>
    <div class="accent-line right"></div>
    <div class="web-band">WWW.MYBLUEBIRDHOSTING.COM</div>
  </main>
</body>
</html>
```